" A Rumo ao Horizonte é uma empresa que trabalha com curso, treinamentos e palestras com o objetivo de desenvolvimento pessoal e aumentar o nível de vibração pessoal. "

```html
<!DOCTYPE html>
<html lang="pt-BR">
<head>
<meta charset="utf-8">
<title>Rumo ao Horizonte — Cartão de visita</title>
<link href="https://fonts.googleapis.com/css2?family=Questrial&display=swap" rel="stylesheet">
<style>
  :root {
    --page-bg: #f4f4f4;
    --card-bg: #e5e6e8;
    --teal: #1f9a86;
    --purple: #6a3a8c;
    --gold: #c9a12a;
    --icon-ink: #ffffff;
  }
  * { margin: 0; padding: 0; box-sizing: border-box; }
  html, body {
    width: 1200px;
    height: 1200px;
    overflow: hidden;
    background: var(--page-bg);
    font-family: "Questrial", "Century Gothic", sans-serif;
  }
  .business-card {
    position: absolute;
    left: 139px;
    top: 444px;
    width: 924px;
    height: 312px;
    background: var(--card-bg);
    border-radius: 36px;
    overflow: hidden;
  }
  .holder-name {
    position: absolute;
    left: 39px;
    top: 56px;
    font-size: 34px;
    font-weight: 400;
    line-height: 42px;
    color: var(--teal);
    letter-spacing: 0.4px;
  }
  .contact-list {
    position: absolute;
    left: 43px;
    top: 170px;
    list-style: none;
  }
  .contact-item {
    display: flex;
    align-items: center;
    height: 31px;
    font-size: 24px;
    color: var(--teal);
  }
  .contact-icon {
    width: 20px;
    height: 20px;
    margin-right: 13px;
    flex: none;
  }
  .brand-name {
    position: absolute;
    left: 500px;
    top: 168px;
    width: 380px;
    text-align: center;
    font-size: 38px;
    line-height: 48px;
    color: var(--purple);
    white-space: nowrap;
  }
</style>
</head>
<body>
  <section class="business-card">
    <h1 class="holder-name">Lúcia Fontes</h1>

    <ul class="contact-list">
      <li class="contact-item">
        <svg class="contact-icon" viewBox="0 0 22 22" aria-hidden="true">
          <rect width="22" height="22" rx="4" fill="var(--gold)"/>
          <rect x="7" y="4" width="8" height="14" rx="1.5" fill="none" stroke="var(--icon-ink)" stroke-width="1.6"/>
          <circle cx="11" cy="15.5" r="0.9" fill="var(--icon-ink)"/>
        </svg>
        <span>31 90000-4521</span>
      </li>
      <li class="contact-item">
        <svg class="contact-icon" viewBox="0 0 22 22" aria-hidden="true">
          <rect width="22" height="22" rx="4" fill="var(--gold)"/>
          <rect x="4.5" y="6.5" width="13" height="9" rx="1" fill="none" stroke="var(--icon-ink)" stroke-width="1.5"/>
          <path d="M4.8 7 L11 11.8 L17.2 7" fill="none" stroke="var(--icon-ink)" stroke-width="1.5"/>
        </svg>
        <span>lucia@rumoaohorizonte.com.br</span>
      </li>
      <li class="contact-item">
        <svg class="contact-icon" viewBox="0 0 22 22" aria-hidden="true">
          <rect width="22" height="22" rx="4" fill="var(--gold)"/>
          <circle cx="11" cy="11" r="6" fill="none" stroke="var(--icon-ink)" stroke-width="1.4"/>
          <ellipse cx="11" cy="11" rx="2.6" ry="6" fill="none" stroke="var(--icon-ink)" stroke-width="1.2"/>
          <line x1="5" y1="11" x2="17" y2="11" stroke="var(--icon-ink)" stroke-width="1.2"/>
        </svg>
        <span>www.rumoaohorizonte.com.br</span>
      </li>
    </ul>

    <p class="brand-name">Rumo ao Horizonte</p>
  </section>
</body>
</html>
```